Tranquilly Balanced Restoration

We want to design a business card that is modern and appealing for an innovative psychedelic telemedicine company that provides at-home ketamine-assisted therapy along with wellness, longevity, and anti-aging medicines. We want to use our deep purple and white plus other colors you can find on our website. We don't have any strict brand guidelines yet so feel free to get creative. We want a very professional, but technology first modern design that will instill trust, peace, calm, but also be attractive to investors in the healthcare and SaaS space.

```html
<!DOCTYPE html>
<html lang="en">
<head>
<meta charset="utf-8">
<title>Tranquilly Balanced Restoration – Business Card</title>
<link href="https://fonts.googleapis.com/css2?family=Open+Sans:wght@400;600;700&display=swap" rel="stylesheet">
<style>
  :root{
    --page:#1c1c20;
    --deep-purple:#2a1840;
    --pattern-purple:#3b2160;
    --orchid:#b57aa9;
    --name-pink:#b864a8;
    --lavender:#7b62ad;
    --white:#ffffff;
  }
  *{box-sizing:border-box;margin:0;padding:0}
  html,body{width:1200px;height:780px;overflow:hidden}
  body{
    background:var(--page);
    font-family:"Open Sans",Arial,sans-serif;
    position:relative;
  }
  .card{
    position:absolute;
    width:540px;height:310px;
    border-radius:22px;
    overflow:hidden;
    box-shadow:0 18px 40px rgba(0,0,0,.45);
  }
  /* back side */
  .card--back{left:40px;top:235px;background:var(--deep-purple)}
  .back-pattern{
    position:absolute;inset:0;
    background:linear-gradient(135deg,var(--deep-purple) 0%,var(--pattern-purple) 50%,var(--deep-purple) 100%);
  }
  .back-brand{
    position:absolute;right:26px;bottom:22px;
    display:flex;align-items:center;gap:8px;
    color:var(--orchid);font-size:13px;font-weight:400;
  }
  .brand-dot{width:14px;height:14px;border-radius:50%;background:var(--lavender)}

  /* front side */
  .card--front{left:620px;top:235px;background:var(--white)}
  .front-wave{position:absolute;inset:0;width:100%;height:100%}
  .front-brand{
    position:absolute;left:268px;top:30px;
    display:flex;align-items:center;gap:12px;
  }
  .front-brand .brand-dot{width:34px;height:34px;flex:none}
  .front-brand-name{color:var(--name-pink);font-size:18px;font-weight:400;line-height:22px;white-space:nowrap}
  .person{position:absolute;left:112px;top:186px}
  .person-name{color:var(--name-pink);font-size:21px;font-weight:700;line-height:1.1;white-space:nowrap}
  .person-role{color:var(--white);font-size:12px;font-weight:400;margin-top:3px;white-space:nowrap}
  .contacts{position:absolute;left:118px;top:240px;list-style:none}
  .contacts li{
    display:flex;align-items:center;gap:8px;
    color:var(--white);font-size:11.5px;line-height:19px;white-space:nowrap;
  }
  .contacts svg{width:11px;height:11px;flex:none}
  .address{
    position:absolute;left:360px;top:196px;
    color:var(--white);font-size:11px;line-height:16px;font-style:normal;white-space:nowrap;
  }
</style>
</head>
<body>

  <section class="card card--back" aria-label="Card back">
    <div class="back-pattern" role="img" aria-label="Repeating brand pattern in purple tones"></div>
    <div class="back-brand"><span class="brand-dot"></span>Tranquilly Balanced Restoration</div>
  </section>

  <section class="card card--front" aria-label="Card front">
    <svg class="front-wave" viewBox="0 0 540 310" preserveAspectRatio="none" aria-hidden="true">
      <path d="M250,146 C360,128 470,118 515,82 C530,70 537,58 540,50 L540,310 L250,310 Z" fill="var(--orchid)"/>
      <path d="M40,310 C15,235 70,168 200,150 C300,136 420,132 495,108 C515,101 532,92 540,86 L540,310 Z" fill="var(--deep-purple)"/>
    </svg>

    <div class="front-brand">
      <span class="brand-dot"></span>
      <span class="front-brand-name">Tranquilly Balanced<br>Restoration</span>
    </div>

    <div class="person">
      <p class="person-name">Maren Ellison, FNP-C</p>
      <p class="person-role">Co-founder, Chief Clinical Officer</p>
    </div>

    <ul class="contacts">
      <li>
        <svg viewBox="0 0 24 24"><path fill="var(--orchid)" d="M6.6 10.8a15.1 15.1 0 0 0 6.6 6.6l2.2-2.2a1 1 0 0 1 1-.25 11.4 11.4 0 0 0 3.6.57 1 1 0 0 1 1 1V20a1 1 0 0 1-1 1A17 17 0 0 1 3 4a1 1 0 0 1 1-1h3.5a1 1 0 0 1 1 1c0 1.250.2 2.450.57 3.570a1 1 0 0 1-.25 1z"/></svg>
        +1 800-555-0142
      </li>
      <li>
        <svg viewBox="0 0 24 24"><circle cx="12" cy="12" r="10" fill="none" stroke="var(--orchid)" stroke-width="2.4"/><path d="M2 12h20M12 2c3 3 3 17 0 20M12 2c-3 3-3 17 0 20" fill="none" stroke="var(--orchid)" stroke-width="2"/></svg>
        www.tranquillybalanced.com
      </li>
      <li>
        <svg viewBox="0 0 24 24"><rect x="2" y="5" width="20" height="14" rx="2" fill="var(--orchid)"/><path d="M2 6l10 7 10-7" fill="none" stroke="var(--deep-purple)" stroke-width="2"/></svg>
        hello@tranquillybalanced.com
      </li>
    </ul>

    <address class="address">
      482 Aspen Way, Suite 210,<br>
      Fairview, CO, United States,<br>
      Colorado
    </address>
  </section>

</body>
</html>
```